Funeral Services Site

We need a website for a Funeral Services company. The old website is: www.rouwcentrumdelvoort.be We need the same structure and text.

Target Market(s)

Customers.

Coding

Coded - Design and coding required

Number of Pages Required

4 page

Font styles to use
Serif
Sans Serif
Script

```html
<!DOCTYPE html>
<html lang="en">
<head>
<meta charset="utf-8">
<title>Funeral home Delvoort bvba</title>
<link href="https://fonts.googleapis.com/css2?family=Bitter:ital,wght@0,400;0,500;1,400;1,500&family=Jost:wght@300;400&family=Arimo:wght@700&family=Kaushan+Script&display=swap" rel="stylesheet">
<style>
:root{
  --ink:#1a1a1a;
  --text:#333;
  --muted:#8a8a8a;
  --white:#fff;
  --hero-dark:#1e1a16;
  --footer:#565656;
  --field:#6e6e6e;
  --field-line:#8a8a8a;
  --button-grey:#555;
}
*{box-sizing:border-box;margin:0;padding:0}
html,body{width:1200px;height:2541px;overflow:hidden;background:var(--white)}
body{position:relative;font-family:'Jost',sans-serif;font-weight:300;color:var(--text)}
.abs{position:absolute}

/* header */
.site-header{position:absolute;left:0;top:0;width:1200px;height:105px;background:var(--white)}
.brand{position:absolute;left:142px;top:28px;display:flex;align-items:center;gap:10px}
.brand-name{font-family:'Bitter',serif;font-weight:500;font-size:23px;line-height:25px;color:var(--ink)}
.brand-mark{width:40px;height:40px;border:2px solid var(--ink);border-radius:50%}
.main-nav{position:absolute;left:482px;top:41px;display:flex;gap:27px;font-family:'Bitter',serif;font-size:14.5px;color:#555}
.main-nav .current{color:var(--ink);font-weight:500}
.nav-divider{position:absolute;left:975px;top:41px;width:1px;height:22px;background:#999}
.lang{position:absolute;left:997px;top:42px;font-family:'Jost',sans-serif;font-size:14.5px;color:#555;display:flex;align-items:center;gap:5px}
.lang .flag{width:18px;height:12px;background:#2a3f8c;border:1px solid #c8102e}

/* hero */
.hero{position:absolute;left:0;top:105px;width:1200px;height:495px;background:radial-gradient(ellipse at 50% 40%,#4a3a2c 0%,#2a221b 55%,var(--hero-dark) 100%)}
.hero-title{position:absolute;left:0;top:172px;width:1200px;text-align:center;font-family:'Arimo',sans-serif;font-weight:700;font-size:34px;line-height:43px;color:var(--white);text-shadow:0 2px 4px rgba(0,0,0,.6)}
.btn{position:absolute;height:39px;display:flex;align-items:center;justify-content:center;font-family:'Bitter',serif;font-size:15.5px}
.btn-light{background:var(--white);color:var(--ink)}
.btn-dark{background:#000;color:var(--white)}
.btn-grey{background:var(--button-grey);color:var(--white)}
.scroll-hint{position:absolute;display:flex;align-items:center;gap:10px;font-size:14.5px}
.hero .scroll-hint{left:142px;top:454px;color:var(--white);font-weight:400}
.dots{position:absolute;left:575px;top:452px;display:flex;gap:11px;align-items:center}
.dots span{width:7px;height:7px;border:1px solid #ddd;border-radius:50%}
.dots .on{width:10px;height:10px;background:var(--white);border:none}

/* about */
.about-photo{position:absolute;left:0;top:686px;width:459px;height:369px;background:linear-gradient(180deg,#6d7478 0%,#4e5a4a 55%,#3a3f35 100%)}
.about-photo p{position:absolute;left:142px;top:86px;width:310px;font-family:'Kaushan Script',cursive;font-size:31px;line-height:51px;color:var(--white)}
.section-title{font-family:'Bitter',serif;font-weight:400;font-size:33px;line-height:41px;color:var(--ink)}
.body-copy{font-size:14.5px;line-height:21.5px;color:#444}
.body-copy strong{font-weight:400;color:var(--ink)}
.about-text{position:absolute;left:495px;top:752px;width:555px}
.about-text .body-copy{margin-top:30px}
.about-text .body-copy + .body-copy{margin-top:11px}
.light-hint{color:var(--muted)}

/* worship */
.worship-text{position:absolute;left:143px;top:1206px;width:470px}
.worship-text .body-copy{margin-top:30px}
.worship-text .body-copy + .body-copy{margin-top:17px}
.service-list{list-style:none;margin-top:13px}
.service-list li{display:flex;align-items:center;gap:16px;font-size:14.5px;line-height:21.5px;color:#444;margin-bottom:14px}
.service-list svg{flex:none}
.worship-photo{position:absolute;left:643px;top:1140px;width:557px;height:631px;background:linear-gradient(135deg,#c9aa8a 0%,#a78465 55%,#8a6b52 100%)}
.bars{position:absolute;left:187px;top:571px;display:flex;gap:8px}
.bars span{width:22px;height:3px;background:#ddd}
.bars .on{width:38px;background:var(--white)}

/* call to action */
.cta{position:absolute;left:0;top:1850px;width:1200px;text-align:center}
.cta-kicker{font-family:'Bitter',serif;font-style:italic;font-size:18px;color:#555}
.cta-title{margin-top:14px;font-family:'Bitter',serif;font-style:italic;font-weight:500;font-size:28px;line-height:40px;letter-spacing:.6px;color:var(--ink)}

/* footer */
.site-footer{position:absolute;left:0;top:2108px;width:1200px;height:433px;background:var(--footer);color:var(--white)}
.footer-head{position:absolute;font-family:'Bitter',serif;font-size:18px;color:var(--white)}
.footer-head::after{content:"";display:block;margin-top:8px;width:100%;height:1px;background:#aaa}
.quick-links{position:absolute;left:145px;top:161px;list-style:none;font-size:13px;font-weight:400}
.quick-links li{line-height:30px;padding-left:17px;position:relative}
.quick-links li::before{content:"";position:absolute;left:0;top:14px;width:3px;height:3px;background:var(--white);border-radius:50%}
.contact-row{position:absolute;left:358px;display:flex;align-items:center;gap:11px;font-size:13px;font-weight:400;line-height:20px}
.contact-row .icon{width:32px;height:32px;border-radius:50%;background:var(--white);display:flex;align-items:center;justify-content:center;flex:none}
.contact-row b{font-family:'Bitter',serif;font-weight:500;font-size:14px}
.field{position:absolute;background:var(--field);border:1px solid var(--field-line);font-size:11.5px;font-weight:400;color:#e8e8e8;padding:8px 7px}
.submit{position:absolute;left:948px;top:2246px;width:112px;height:59px;background:#f3f3f3;color:var(--ink);font-family:'Bitter',serif;font-weight:500;font-size:17px;line-height:21px;text-align:center;padding-top:9px;top:246px}
.copyright{position:absolute;left:0;top:383px;width:1200px;text-align:center;font-size:13px;font-weight:400}
</style>
</head>
<body>

<header class="site-header">
  <div class="brand">
    <div class="brand-name">Funeral home<br>Delvoort bvba</div>
    <span class="brand-mark"></span>
  </div>
  <nav class="main-nav">
    <span class="current">Home</span><span>About Us</span><span>Condole Online</span><span>Order Flowers</span><span>Contact</span>
  </nav>
  <span class="nav-divider"></span>
  <div class="lang"><span class="flag"></span>Eng
    <svg width="8" height="6" viewBox="0 0 8 6"><path d="M1 1l3 3 3-3" fill="none" stroke="#777"/></svg>
  </div>
</header>

<section class="hero" role="img" aria-label="Photo of a crowd holding candles at an evening vigil">
  <h1 class="hero-title">Funeral home Delvoort bvba:<br>a Personal Service in Farewell Guidance</h1>
  <span class="btn btn-light" style="left:424px;top:278px;width:155px">011 20 34 56</span>
  <span class="btn btn-light" style="left:599px;top:278px;width:177px">Contact Us Today</span>
  <div class="scroll-hint">
    <svg width="10" height="16" viewBox="0 0 10 16"><path d="M5 0v14M1 10l4 4 4-4" fill="none" stroke="#fff" stroke-width="1.3"/></svg>
    scroll down to About us
  </div>
  <div class="dots"><span></span><span class="on"></span><span></span></div>
</section>

<section>
  <div class="about-photo" role="img" aria-label="Photo of the funeral home building among trees">
    <p>Mourning Center Delvoort, A Complete Service In Mourning And Farewell Guidance</p>
  </div>
  <div class="about-text">
    <h2 class="section-title">About Us</h2>
    <p class="body-copy">Saying goodbye to a loved one is one of the toughest things in a lifetime. Funeral home Delvoort in Hoeven takes care of <strong>all the practical and administrative matters</strong> involved. So you can say goodbye in peace.</p>
    <p class="body-copy">Our people have a r uime experience in farewell guidance and stand for 24 hours at 24 hours for you. Our fully renovated funeral home is open to you and your acquaintances, so that you can greet your loved one at any time of the day.</p>
    <div class="scroll-hint light-hint" style="position:relative;margin-top:28px">
      <svg width="10" height="16" viewBox="0 0 10 16"><path d="M5 0v14M1 10l4 4 4-4" fill="none" stroke="#333" stroke-width="1.3"/></svg>
      scroll down to funeral and worship
    </div>
  </div>
</section>

<section>
  <div class="worship-text">
    <h2 class="section-title">Organization Funeral and Worship</h2>
    <p class="body-copy">The organization of the funeral ceremony is a moment of reflection, where the personality of the deceased can be beautifully highlighted. Our team will assist you in this and select the most beautiful texts, songs and photos with you in order to arrive at an appropriate and worthy goodbye.</p>
    <p class="body-copy">The funeral can take place in your parish church or our auditorium if you wish, which can accommodate a maximum of 100 guests. We can arrange the following for you:</p>
    <ul class="service-list">
      <li><svg width="42" height="42" viewBox="0 0 42 42"><circle cx="21" cy="21" r="20" fill="none" stroke="#555"/><rect x="18.5" y="17" width="5" height="14" fill="none" stroke="#555"/><path d="M21 11c2 2 2 4 0 5c-2-1-2-3 0-5z" fill="none" stroke="#555"/></svg>Vigil the Night Before the Funeral</li>
      <li><svg width="42" height="42" viewBox="0 0 42 42"><circle cx="21" cy="21" r="20" fill="none" stroke="#555"/><circle cx="21" cy="16" r="5" fill="none" stroke="#555"/><path d="M12 31c1-6 5-8 9-8s8 2 9 8z" fill="none" stroke="#555"/></svg>Prayer Service with Priest ( If Possible )</li>
      <li><svg width="42" height="42" viewBox="0 0 42 42"><circle cx="21" cy="21" r="20" fill="none" stroke="#555"/><path d="M14 13h14c0 6-3 9-7 9s-7-3-7-9zM21 22v7M16 30h10" fill="none" stroke="#555"/></svg>Eucharistic Celebration with Priest ( On Tuesday and Friday in the Parishes of Hoeven)</li>
    </ul>
    <div class="scroll-hint light-hint" style="position:relative;margin:42px 0 0 235px">
      <svg width="10" height="16" viewBox="0 0 10 16"><path d="M5 0v14M1 10l4 4 4-4" fill="none" stroke="#333" stroke-width="1.3"/></svg>
      scroll down to contact us
    </div>
  </div>
  <div class="worship-photo" role="img" aria-label="Photo of ceramic roses in black and white on metal stems">
    <div class="bars"><span class="on"></span><span></span><span></span></div>
  </div>
</section>

<section class="cta">
  <p class="cta-kicker">We are here for you.</p>
  <h2 class="cta-title">DO YOU HAVE ANY QUESTIONS OR WOULD YOU LIKE TO CALL IN<br>OUR FUNERAL HOME? - CONTACT US.</h2>
  <span class="btn btn-dark" style="left:424px;top:136px;width:155px">011 20 34 56</span>
  <span class="btn btn-grey" style="left:599px;top:136px;width:177px">Contact Us Today</span>
</section>

<footer class="site-footer">
  <h3 class="footer-head" style="left:145px;top:112px;width:121px">Quick Links</h3>
  <ul class="quick-links">
    <li>Home</li><li>About Us</li><li>Condole Online</li><li>Order Flowers</li><li>Contact</li>
  </ul>

  <h3 class="footer-head" style="left:362px;top:112px;width:128px">Contact Details</h3>
  <div class="contact-row" style="top:162px">
    <span class="icon"><svg width="14" height="18" viewBox="0 0 14 18"><path d="M7 17s6-6 6-10A6 6 0 0 0 1 7c0 4 6 10 6 10z" fill="#555"/><circle cx="7" cy="7" r="2.2" fill="#fff"/></svg></span>
    <div><b>Rouwcentrum Delvoort</b> <small style="font-size:7px">bvba</small><br>Lindeweg 14, 3700 Hoeven (Tongeren)</div>
  </div>
  <div class="contact-row" style="top:222px">
    <span class="icon"><svg width="16" height="16" viewBox="0 0 16 16"><path d="M3 1l3 3-2 2c1 2 4 5 6 6l2-2 3 3-2 2C7 15 1 9 1 3z" fill="#555"/></svg></span>
    <div>011 20 34 56 ( 24/24, 7 out of 7 )</div>
  </div>
  <div class="contact-row" style="top:276px">
    <span class="icon"><svg width="14" height="10" viewBox="0 0 14 10"><rect width="14" height="10" fill="#555"/><path d="M0 0l7 5 7-5" fill="none" stroke="#fff"/></svg></span>
    <div>mourning.center.delvoort@mail.be</div>
  </div>

  <h3 class="footer-head" style="left:712px;top:111px;width:123px">Quick Inquiry</h3>
  <div class="field" style="left:713px;top:159px;width:165px;height:32px">First Name</div>
  <div class="field" style="left:894px;top:159px;width:166px;height:32px">Last Name</div>
  <div class="field" style="left:713px;top:202px;width:165px;height:32px">Phone</div>
  <div class="field" style="left:894px;top:202px;width:166px;height:32px">Email</div>
  <div class="field" style="left:713px;top:246px;width:218px;height:59px">Message</div>
  <div class="submit">SUBMIT<br>NOW</div>

  <p class="copyright">Copyright 2019 Rouwcentrum Delvoort bvba. All Rights Reserved</p>
</footer>

</body>
</html>
```